Supplement Bottle Packaging and Design

We want to rebrand our current health supplements (see below). We do want it to be modern, vibrant and appealing supplement bottles. Very upscale and elegant as it targets primarily women.
NOTE: READ THE ATTACHED WORD DOCUMENT!
Bottle size: We are totally open to the bottle size and shape, as long it's a typical supplement bottle size to handle 90-120 capsules; what we mostly need is new bottle design/packaging. YOU DON’T HAVE TO USE THE CURRENT WHITE BOTTLE SHAPE, BUT ANYTHING MORE MODERN WOULD WORK!
Updates
We need more modern, clean sleek designs to choose from
Look and feel
Each slider illustrates characteristics of the customer's brand and the style your logo design should communicate.

```html
<!DOCTYPE html>
<html lang="en">
<head>
<meta charset="utf-8">
<title>Aura Supplement Range</title>
<link rel="stylesheet" href="https://fonts.googleapis.com/css2?family=Montserrat:wght@400;600;700;800&display=swap">
<style>
  :root{
    --bg:#ffffff;
    --white:#ffffff;
    --teal-cap:#1fa595; --teal-body:#137f74; --teal-label:#1db3a3; --teal-label-dark:#148f82; --teal-tab:#5edccd;
    --blue-cap:#2b2fc9; --blue-body:#14158a; --blue-label:#2c2fc7; --blue-label-dark:#1c1ea0; --blue-tab:#4a4ef0;
    --purple-cap:#8b3fb1; --purple-body:#5a1f7c; --purple-label:#9446b8; --purple-label-dark:#6d2a92; --purple-tab:#c25ee0;
    --red-cap:#d3181f; --red-body:#8e0d12; --red-label:#d51d22; --red-label-dark:#ad1317; --red-tab:#f04a4f;
  }
  *{box-sizing:border-box;margin:0;padding:0}
  html,body{width:888px;height:1200px;overflow:hidden;background:var(--bg)}
  body{position:relative;font-family:"Montserrat",Arial,sans-serif;color:var(--white)}

  .bottle{position:absolute;width:269px;height:506px}
  .bottle--hormone{left:121px;top:78px;--cap:var(--teal-cap);--body:var(--teal-body);--label:var(--teal-label);--label-dark:var(--teal-label-dark);--tab:var(--teal-tab)}
  .bottle--sugar{left:484px;top:78px;--cap:var(--blue-cap);--body:var(--blue-body);--label:var(--blue-label);--label-dark:var(--blue-label-dark);--tab:var(--blue-tab)}
  .bottle--liver{left:121px;top:645px;--cap:var(--purple-cap);--body:var(--purple-body);--label:var(--purple-label);--label-dark:var(--purple-label-dark);--tab:var(--purple-tab)}
  .bottle--tummy{left:484px;top:645px;--cap:var(--red-cap);--body:var(--red-body);--label:var(--red-label);--label-dark:var(--red-label-dark);--tab:var(--red-tab)}

  .bottle__cap{position:absolute;left:20px;top:0;width:229px;height:70px;border-radius:10px 10px 4px 4px;background:var(--cap)}
  .bottle__neck{position:absolute;left:40px;top:68px;width:189px;height:40px;background:var(--body);opacity:.85}
  .bottle__body{position:absolute;left:0;top:100px;width:269px;height:406px;border-radius:34px 34px 30px 30px;background:var(--body)}

  .label{position:absolute;left:0;top:126px;width:269px;height:353px;overflow:hidden;
    background:linear-gradient(90deg,var(--label) 0%,var(--label-dark) 55%,var(--label) 100%);
    display:flex;flex-direction:column;align-items:center;text-align:center}
  .label__icon{position:absolute;left:-38px;width:150px;height:150px}
  .label__title{margin-top:20px;font-weight:700;font-size:54px;line-height:1.05;letter-spacing:-1px;position:relative}
  .label__title--narrow .label__title-top{font-size:44px;letter-spacing:-1.5px}
  .label__title-top{display:block}
  .label__claim{position:relative;font-weight:700;font-size:24px;line-height:1.1;margin-top:18px}
  .label__type{position:absolute;top:280px;left:0;width:100%;font-size:13px;letter-spacing:3.2px;font-weight:400}
  .label__count{position:absolute;top:313px;left:43px;width:183px;height:40px;border-radius:18px 18px 0 0;
    background:var(--tab);font-weight:700;font-size:15px;line-height:20px;letter-spacing:.5px;padding-top:1px}
  .label__count-band{position:absolute;top:332px;left:0;width:100%;height:21px;background:var(--tab)}
</style>
</head>
<body>

<div class="bottle bottle--hormone">
  <div class="bottle__cap"></div><div class="bottle__neck"></div><div class="bottle__body"></div>
  <div class="label">
    <svg class="label__icon" style="top:132px" viewBox="0 0 150 150" role="img" aria-label="Molecule line icon inside concentric rings">
      <circle cx="75" cy="75" r="70" fill="none" stroke="#4ee3d2" stroke-width="2" opacity=".7"/>
      <circle cx="75" cy="75" r="60" fill="none" stroke="#4ee3d2" stroke-width="1.5" opacity=".5"/>
    </svg>
    <h2 class="label__title"><span class="label__title-top">Hormone</span>Aura</h2>
    <p class="label__claim">Supports<br>Healthy<br>Hormone<br>Levels*</p>
    <p class="label__type">DIETARY SUPPLEMENT</p>
    <div class="label__count-band"></div>
    <p class="label__count">60 VEGETABLE<br>CAPSULES</p>
  </div>
</div>

<div class="bottle bottle--sugar">
  <div class="bottle__cap"></div><div class="bottle__neck"></div><div class="bottle__body"></div>
  <div class="label">
    <svg class="label__icon" style="top:132px" viewBox="0 0 150 150" role="img" aria-label="Liver line icon inside concentric rings">
      <circle cx="75" cy="75" r="70" fill="none" stroke="#4f55ff" stroke-width="2" opacity=".7"/>
      <circle cx="75" cy="75" r="60" fill="none" stroke="#4f55ff" stroke-width="1.5" opacity=".5"/>
    </svg>
    <h2 class="label__title label__title--narrow"><span class="label__title-top">Blood Sugar</span>Aura</h2>
    <p class="label__claim" style="margin-top:22px">Supports<br>Healthy<br>Blood Glucose<br>Levels*</p>
    <p class="label__type">DIETARY SUPPLEMENT</p>
    <div class="label__count-band"></div>
    <p class="label__count">60 VEGETABLE<br>CAPSULES</p>
  </div>
</div>

<div class="bottle bottle--liver">
  <div class="bottle__cap"></div><div class="bottle__neck"></div><div class="bottle__body"></div>
  <div class="label">
    <svg class="label__icon" style="top:150px" viewBox="0 0 150 150" role="img" aria-label="Liver line icon inside concentric rings">
      <circle cx="75" cy="75" r="70" fill="none" stroke="#c070e6" stroke-width="2" opacity=".7"/>
      <circle cx="75" cy="75" r="60" fill="none" stroke="#c070e6" stroke-width="1.5" opacity=".5"/>
    </svg>
    <h2 class="label__title" style="margin-top:30px"><span class="label__title-top">Liver</span>Aura</h2>
    <p class="label__claim" style="margin-top:16px">Rejuvenating<br>Cleanse<br>&amp; Detox<br>Formula*</p>
    <p class="label__type" style="top:286px">DIETARY SUPPLEMENT</p>
    <div class="label__count-band"></div>
    <p class="label__count">120 VEGETABLE<br>CAPSULES</p>
  </div>
</div>

<div class="bottle bottle--tummy">
  <div class="bottle__cap"></div><div class="bottle__neck"></div><div class="bottle__body"></div>
  <div class="label">
    <svg class="label__icon" style="top:150px" viewBox="0 0 150 150" role="img" aria-label="Stomach line icon inside concentric rings">
      <circle cx="75" cy="75" r="70" fill="none" stroke="#f25055" stroke-width="2" opacity=".7"/>
      <circle cx="75" cy="75" r="60" fill="none" stroke="#f25055" stroke-width="1.5" opacity=".5"/>
    </svg>
    <h2 class="label__title" style="margin-top:30px"><span class="label__title-top">Tummy</span>Aura</h2>
    <p class="label__claim" style="margin-top:16px">Oxygenating<br>Colon<br>Cleanse*</p>
    <p class="label__type" style="top:286px">DIETARY SUPPLEMENT</p>
    <div class="label__count-band"></div>
    <p class="label__count">90 VEGETABLE<br>CAPSULES</p>
  </div>
</div>

</body>
</html>
```